KWI Business Card

Please create a creative design for a business card using the new theme from the Logo & website. This company's main focus is food manufacturing building construction. Please integrate the new logo attached.

Please use the following information for the demo card:

Korvel Walls, Inc.
Dana Whitcombe
dwhitcombe@korvelwalls.example
Cell: 312-555-0178
218 Larkmoor Ave
Fenwick Glen, WI 60418

See pictures and more information on the website.

www.korvelwalls.example

```html
<!DOCTYPE html>
<html lang="en">
<head>
<meta charset="utf-8">
<title>KWI Business Card</title>
<link rel="stylesheet" href="https://fonts.googleapis.com/css2?family=Montserrat:wght@400;600&family=Michroma&display=swap">
<style>
  :root {
    --backdrop: #2b2b2b;
    --card: #141414;
    --blue: #3f86d8;
    --silver: #c9c9c9;
    --white: #f2f2f2;
  }
  * { margin: 0; padding: 0; box-sizing: border-box; }
  html, body { width: 1200px; height: 901px; overflow: hidden; }
  body {
    background: var(--backdrop);
    font-family: "Montserrat", sans-serif;
    display: flex;
    flex-direction: column;
    align-items: center;
    justify-content: center;
    gap: 40px;
  }
  .card {
    width: 680px;
    height: 388px;
    background: var(--card);
    position: relative;
    box-shadow: 0 10px 30px rgba(0,0,0,0.45);
  }
  .brand {
    display: flex;
    flex-direction: column;
    align-items: flex-start;
  }
  .brand-name { font-weight: 600; letter-spacing: 0.06em; line-height: 1; }
  .brand-sub { font-weight: 600; letter-spacing: 0.06em; }
  .brand-tagline { font-weight: 600; letter-spacing: 0.1em; margin-top: 8px; }

  /* back side */
  .card-back { display: flex; align-items: center; justify-content: center; }
  .card-back .brand-name { font-size: 62px; color: var(--silver); }
  .card-back .brand-sub { font-size: 30px; color: var(--silver); margin-top: 10px; }
  .card-back .brand-tagline { font-size: 18px; color: var(--silver); }

  /* front side */
  .card-front .brand { position: absolute; left: 80px; top: 52px; }
  .card-front .brand-name { font-size: 48px; color: var(--blue); }
  .card-front .brand-sub { font-size: 22px; color: var(--blue); margin-top: 8px; }
  .card-front .brand-tagline { font-size: 13px; color: var(--blue); }

  .contact { position: absolute; left: 50px; right: 40px; top: 250px; }
  .person-name {
    font-family: "Michroma", sans-serif;
    font-size: 22px;
    font-weight: 400;
    letter-spacing: 0.14em;
    color: var(--blue);
    text-transform: uppercase;
  }
  .rule { height: 1px; background: var(--white); margin: 8px 0 12px; }
  .contact-line {
    font-size: 13px;
    color: var(--white);
    line-height: 1.9;
    white-space: nowrap;
  }
  .label { color: var(--blue); margin-right: 4px; }
  .sep { margin: 0 8px; }
</style>
</head>
<body>
  <section class="card card-back">
    <div class="brand">
      <span class="brand-name">KWI</span>
      <span class="brand-sub">Korvel Walls, Inc.</span>
      <span class="brand-tagline">cold storage construction</span>
    </div>
  </section>

  <section class="card card-front">
    <div class="brand">
      <span class="brand-name">KWI</span>
      <span class="brand-sub">Korvel Walls, Inc.</span>
      <span class="brand-tagline">cold storage construction</span>
    </div>
    <div class="contact">
      <h1 class="person-name">Dana Whitcombe</h1>
      <div class="rule"></div>
      <p class="contact-line">218 Larkmoor Ave, Fenwick Glen, WI 60418</p>
      <p class="contact-line"><span class="label">P :</span>312-555-0178<span class="sep">|</span><span class="label">E :</span>dwhitcombe@korvelwalls.example<span class="sep">|</span><span class="label">W :</span>www.korvelwalls.example</p>
    </div>
  </section>
</body>
</html>
```